Business Cards Needed for Innovative Healthcare Marketing Company

We are a marketing company focused on healthcare. Our company is all about rebranding yourself renewing your image and generating results. The phoenix stands for "reborn" or "rising" which we provide new brands for our clients we take their old brands and renew it with creativity and innovation. I am looking for a business card with color dimension. I have attached an example of a card I think has the look and feel of what I am trying to accomplish. I like that the card example has black and grey font colors, I like the font placement and the small logo, I really like the use of the colors on the right those are the colors of my logo. My logo is phoenix so maybe incorporating flames similar to that design. I would like the back a solid color maybe red with an opaque version of the logo and website. As a marketing company I am always open to creative liberty!

Target Market(s)

Doctors and business professionals.

Industry/Entity Type

Marketing

Contact Information for Business Card

Velmora Health Care Marketing
Dana Prewitt- CEO
#(407)555-0172
email-dana@velmora.com
website- velmora.com

Font styles to use
Sans Serif

Colors
ec1f27
f37122
ffc214
fbed22
fbf289
f04a50

Requirements
Must have
• The logo and required information
Nice to have
• icons by the information
Should not have
• child like font

```html
<!DOCTYPE html>
<html lang="en">
<head>
<meta charset="utf-8">
<title>Velmora Health Care Marketing – Business Card</title>
<link href="https://fonts.googleapis.com/css2?family=Open+Sans:wght@400;600;700&family=Raleway:wght@300&display=swap" rel="stylesheet">
<style>
  :root {
    --stage: #e8e5e1;
    --card: #ffffff;
    --brand-red: #9e2328;
    --brand-orange: #ef7b22;
    --ink: #2e2e2e;
    --rule: #c9c9c9;
    --white: #ffffff;
  }
  * { box-sizing: border-box; margin: 0; padding: 0; }
  html, body { width: 1200px; height: 1000px; overflow: hidden; }
  body { background: var(--stage); position: relative; font-family: "Open Sans", Arial, sans-serif; color: var(--ink); }

  .card {
    position: absolute; left: 265px; width: 665px; height: 397px;
    background: var(--card); border-radius: 24px; overflow: hidden;
    box-shadow: 0 6px 16px rgba(0,0,0,.18);
  }
  .card--front { top: 73px; }
  .card--back { top: 533px; }

  .brand { position: absolute; display: flex; align-items: center; }
  .brand__dot { border-radius: 50%; background: var(--brand-orange); flex: none; }
  .brand__text { font-family: "Raleway", Arial, sans-serif; font-weight: 300; color: var(--brand-red); line-height: 1; }
  .brand__name { display: block; letter-spacing: 1px; }
  .brand__tag { display: block; letter-spacing: .5px; }

  .card--front .brand { left: 325px; top: 52px; }
  .card--front .brand__dot { width: 62px; height: 62px; margin-right: 18px; }
  .card--front .brand__name { font-size: 52px; }
  .card--front .brand__tag { font-size: 17px; margin-top: 14px; }

  .holder { position: absolute; left: 33px; top: 177px; }
  .holder__name { font-weight: 700; font-size: 20px; color: var(--brand-red); letter-spacing: .3px; }
  .holder__role { font-size: 16px; margin-top: 2px; }

  .divider { position: absolute; left: 33px; top: 238px; width: 452px; height: 1px; background: var(--rule); }

  .address { position: absolute; left: 33px; top: 251px; font-size: 16px; line-height: 24px; font-style: normal; }

  .contacts { position: absolute; right: 30px; top: 227px; list-style: none; text-align: right; font-size: 16px; line-height: 27px; }
  .contacts li { display: flex; align-items: center; justify-content: flex-end; gap: 6px; }
  .contacts svg { width: 14px; height: 14px; fill: var(--brand-red); }

  .wave { position: absolute; left: 0; bottom: 0; width: 665px; height: 100px; }
  .front-web { position: absolute; right: 30px; bottom: 27px; color: var(--white); font-size: 16px; letter-spacing: .3px; }

  .card--back .brand { left: 130px; top: 140px; }
  .card--back .brand__dot { width: 90px; height: 90px; margin-right: 26px; }
  .card--back .brand__name { font-size: 66px; }
  .card--back .brand__tag { font-size: 21px; margin-top: 16px; }
  .back-web { position: absolute; left: 0; right: 0; top: 347px; text-align: center; font-size: 16px; letter-spacing: 1px; }
</style>
</head>
<body>

<section class="card card--front" aria-label="Business card front">
  <div class="brand">
    <span class="brand__dot"></span>
    <span class="brand__text">
      <span class="brand__name">VELMORA</span>
      <span class="brand__tag">HEALTH CARE MARKETING</span>
    </span>
  </div>

  <div class="holder">
    <p class="holder__name">DANA PREWITT</p>
    <p class="holder__role">CEO</p>
  </div>

  <div class="divider"></div>

  <address class="address">
    Level 29, 4 Marlow Tower<br>
    Sydney, 20, New South Wales
  </address>

  <ul class="contacts">
    <li>(407)555-0172
      <svg viewBox="0 0 16 16" aria-hidden="true"><path d="M2 5c0-2 2-3 6-3s6 1 6 3v1h-3V5H5v1H2z M4 7h8l2 6H2z"/></svg>
    </li>
    <li>dana@velmora.com
      <svg viewBox="0 0 16 16" aria-hidden="true"><path d="M1 4h14v9H1z M2 5l6 4 6-4" stroke="#fff" stroke-width="1"/></svg>
    </li>
  </ul>

  <svg class="wave" viewBox="0 0 665 100" preserveAspectRatio="none" aria-hidden="true">
    <defs>
      <linearGradient id="bandGrad" x1="0" x2="1" y1="0" y2="0">
        <stop offset="0" stop-color="#f59a23"/>
        <stop offset=".6" stop-color="#e26a22"/>
        <stop offset="1" stop-color="#a6262a"/>
      </linearGradient>
    </defs>
    <path d="M0,60 C150,80 300,62 400,47 C500,32 600,20 665,30 L665,100 L0,100 Z" fill="url(#bandGrad)"/>
    <path d="M0,20 C120,28 250,40 345,43 C250,48 120,52 0,50 Z" fill="var(--brand-red)"/>
  </svg>
  <p class="front-web">www.<strong>velmora</strong>.com</p>
</section>

<section class="card card--back" aria-label="Business card back">
  <div class="brand">
    <span class="brand__dot"></span>
    <span class="brand__text">
      <span class="brand__name">VELMORA</span>
      <span class="brand__tag">HEALTH CARE MARKETING</span>
    </span>
  </div>
  <p class="back-web">www.velmora.com</p>
</section>

</body>
</html>
```